Plumbing business looking for a website update / to stand out

Looking to update the website with WordPress so looking for a WordPress template customised to our needs. The current website is http://www.corwinhaleplumbing.com.au/ and would like to keep the colour scheme of the green and grey. Like the idea of have menu across the top with drop down menus once mouse is over them.

Looking to stand out and look professional when compared to the competition
http://www.redgroveplumbing.net.au/
http://www.tovisplumbing.com.au/

```html
<!DOCTYPE html>
<html lang="en">
<head>
<meta charset="utf-8">
<title>Corwin Hale Plumbing</title>
<link href="https://fonts.googleapis.com/css2?family=Open+Sans:wght@400;600;700&display=swap" rel="stylesheet">
<style>
:root{
  --green:#8cc63f;
  --green-dark:#6fa82a;
  --nav:#333537;
  --footer:#3d3f41;
  --footer-dark:#2a2b2c;
  --text:#555;
  --muted:#888;
  --line:#dcdcdc;
  --bg:#ffffff;
}
*{box-sizing:border-box;margin:0;padding:0}
html,body{width:863px;height:1200px;overflow:hidden;background:var(--bg)}
body{font-family:"Open Sans",Arial,sans-serif;color:var(--text);font-size:9px;line-height:1.45;position:relative}
.wrap{position:absolute;left:59px;width:745px}
.header{top:0;height:88px;display:flex;align-items:center;justify-content:space-between}
.brand{display:flex;align-items:center;gap:10px}
.brand-dot{width:44px;height:44px;border-radius:50%;background:var(--green)}
.brand-name{font-size:17px;font-weight:600;color:#4a4a4a}
.header-right{text-align:right}
.phone{display:flex;align-items:center;gap:6px;justify-content:flex-end;font-size:13px;color:var(--green);font-weight:600}
.social{display:flex;gap:5px;justify-content:flex-end;margin-bottom:6px}
.social span{width:16px;height:16px;border-radius:50%;background:#9a9a9a}
.nav{position:absolute;top:92px;left:0;width:863px;height:34px;background:var(--nav)}
.nav ul{list-style:none;display:flex;position:absolute;left:160px;height:34px}
.nav li{color:#eee;font-size:12px;padding:0 22px;line-height:34px;border-right:1px solid #474a4c}
.nav li.active{background:var(--green);color:#fff}
.slider{top:140px;height:262px;border:1px solid var(--line);padding:6px}
.slide{width:100%;height:100%;background:linear-gradient(120deg,#f2f2f2 0%,#d9dcdc 40%,#c98a52 60%,#e9ecec 85%)}
.dots{top:416px;display:flex;justify-content:center;gap:7px}
.dots span{width:8px;height:8px;border-radius:50%;background:#bbb}
.dots span:first-child{background:#666}
.features{top:444px;display:flex;gap:22px}
.feature{flex:1;border:1px solid var(--line);padding:6px;height:212px}
.feature-img{height:88px;background:linear-gradient(135deg,#cfd6c4,#8cc63f 70%,#6b7a5e)}
.feature h3{font-size:13px;font-weight:400;color:#444;margin:8px 0 4px;border-bottom:1px solid var(--line);padding-bottom:4px}
.feature p{font-size:8px;color:var(--muted)}
.feature a{color:var(--green);text-decoration:none}
.intro{top:680px;display:flex;gap:40px}
.welcome{width:500px}
.welcome h2,.member h2{font-size:22px;font-weight:400;color:#444;margin-bottom:10px}
.welcome h2 span{color:var(--green)}
.welcome p{font-size:8px;color:var(--muted);margin-bottom:9px}
.member{flex:1}
.badges{border:1px solid var(--line);height:176px;display:flex;align-items:center;justify-content:center;gap:18px}
.badge-round{width:90px;height:90px;border-radius:50%;background:#c9d9e8}
.badge-square{width:90px;height:60px;background:var(--green)}
.footer{position:absolute;top:975px;left:0;width:863px;height:205px;background:var(--footer);color:#ddd}
.footer .cols{position:absolute;left:59px;width:745px;top:14px;display:flex;gap:40px}
.footer h4{font-size:15px;font-weight:400;color:#fff;border-bottom:1px solid #5a5c5e;padding-bottom:4px;margin-bottom:8px}
.menu{width:200px}
.menu li{list-style:none;font-size:9px;line-height:16px;color:#ccc}
.menu li:first-child{color:var(--green)}
.contact{width:250px}
.contact p{display:flex;align-items:center;gap:7px;font-size:9px;line-height:18px}
.contact i{width:11px;height:11px;border-radius:50%;background:var(--green);display:inline-block}
.contact .social{justify-content:flex-start;margin-top:6px}
.contact .social span{background:var(--green);width:18px;height:18px}
.touch{flex:1}
.field{background:#fff;height:15px;margin-bottom:6px;font-size:8px;color:#999;padding:2px 5px}
.field.msg{height:40px}
.submit{background:var(--green);color:#fff;font-size:9px;width:52px;text-align:center;padding:3px 0;margin-left:auto}
.copy{position:absolute;top:1180px;left:0;width:863px;height:20px;background:var(--footer-dark);color:#bbb;font-size:8px;line-height:20px;padding-left:59px}
</style>
</head>
<body>
<header class="wrap header">
  <div class="brand"><div class="brand-dot"></div><div class="brand-name">Corwin Hale Plumbing</div></div>
  <div class="header-right">
    <div class="social"><span></span><span></span><span></span></div>
    <div class="phone">
      <svg width="14" height="14" viewBox="0 0 24 24"><path fill="#8cc63f" d="M6.6 10.8a15 15 0 0 0 6.6 6.6l2.2-2.2c.3-.3.7-.4 1-.2 1.1.4 2.3.6 3.6.6.6 0 1 .4 1 1V20c0 .6-.4 1-1 1A17 17 0 0 1 3 4c0-.6.4-1 1-1h3.5c.6 0 1 .4 1 1 0 1.3.2 2.5.6 3.6.1.3 0 .7-.2 1z"/></svg>
      TELEPHONE (02) 9555 0142
    </div>
  </div>
</header>
<nav class="nav"><ul><li class="active">Home</li><li>Services</li><li>team</li><li>warranty agent</li><li>contact us</li></ul></nav>
<section class="wrap slider"><div class="slide" role="img" aria-label="Copper pipe fittings laid over plumbing plans"></div></section>
<div class="wrap dots"><span></span><span></span><span></span><span></span></div>
<section class="wrap features">
  <article class="feature"><div class="feature-img" role="img" aria-label="Plumbing services photo"></div><h3>Services</h3><p>We offer a full range of plumbing services including hot water, drainage, gas fitting, roofing and guttering across the South West area and surrounding suburbs. <a href="#">Learn More</a></p></article>
  <article class="feature"><div class="feature-img" role="img" aria-label="Plumbing team at work"></div><h3>Team</h3><p>We offer a full range of plumbing services including hot water, drainage, gas fitting, roofing and guttering across the South West area and surrounding suburbs. <a href="#">Learn More</a></p></article>
  <article class="feature"><div class="feature-img" role="img" aria-label="Tap and sink photo"></div><h3>Contact</h3><p>We offer a full range of plumbing services including hot water, drainage, gas fitting, roofing and guttering across the South West area and surrounding suburbs. <a href="#">Learn More</a></p></article>
</section>
<section class="wrap intro">
  <div class="welcome">
    <h2>Welcome to <span>Corwin Hale</span></h2>
    <p>Corwin Hale Plumbing Pty Ltd was established in 1998 and is known for high quality service that employs 2 qualified plumbing tradesmen, 2 apprentices and a fully accredited plumbing company in the commercial and residential sectors of plumbing and maintenance.</p>
    <p>As a locally owned business our commercial and maintenance company, we are committed to providing the best practice that will keep us as a leader in the competitive and challenging market, delivering quality customer service to our clients.</p>
    <p>Committed to training our apprentices, we have 2 apprentices learning the trade under our direction to ensure our clients have only the most up to date skills and techniques available in every field of work.</p>
    <p>We are members of the Hartvale Plumbing Guild and ensure all work is carried out under the rules of the Regional Trade Licensing Council and current building codes.</p>
  </div>
  <div class="member">
    <h2>Member</h2>
    <div class="badges"><div class="badge-round"></div><div class="badge-square"></div></div>
  </div>
</section>
<footer class="footer">
  <div class="cols">
    <div class="menu"><h4>Main Menu</h4><ul><li>Home</li><li>Services</li><li>Team</li><li>Warranty Agent</li><li>Contact</li></ul></div>
    <div class="contact"><h4>Contact Us</h4>
      <p><i></i>Telephone: (02) 9555 0142</p>
      <p><i></i>Fax: (02) 9555 0143</p>
      <p><i></i>E-mail: info@corwinhaleplumbing.com.au</p>
      <p><i></i>www.corwinhaleplumbing.com.au</p>
      <div class="social"><span></span><span></span><span></span><span></span></div>
    </div>
    <div class="touch"><h4>Get in Touch</h4>
      <div class="field">Name</div><div class="field">Email</div><div class="field msg">Message</div>
      <div class="submit">Submit</div>
    </div>
  </div>
</footer>
<div class="copy">Copyright © Corwin Hale Plumbing 2011</div>
</body>
</html>
```